Branding website for a Data Science company with 1 product

Branding website for a Data Science company, featuring our main product: Quorlink. The purpose of the website is to get potential clients to get a peek at what we do, but the main purpose is to get them to get in touch with us. The website will not answer all questions. Therefore the contact details and contact form is a must-have .

Target Market(s)

Potential new B2B clients with medium to large websites, application users (behind a login)

Industry/Entity Type

It Company

Coding

Coded - Design and coding required

Number of Pages Required

2 page

Font styles to use
Sans Serif

Colors

Designer to choose colors to be used in the design.

Requirements
Must have
• A contact form and branding a product

```html
<!DOCTYPE html>
<html lang="en">
<head>
<meta charset="utf-8">
<title>Tallyform Partners – Quorlink</title>
<link rel="stylesheet" href="https://fonts.googleapis.com/css2?family=Archivo+Black&family=Libre+Franklin:wght@400;500;600;700&family=Montserrat:wght@500&display=swap">
<style>
:root{
  --orange:#f04e1c;
  --grey-text:#555;
  --grey-head:#8a8a8a;
  --grey-light:#cfcfcf;
  --line:#8c8c8c;
  --hero-bg:#f6f6f6;
  --white:#fff;
}
*{margin:0;padding:0;box-sizing:border-box}
html,body{width:1200px;height:1173px;overflow:hidden;background:var(--white)}
body{position:relative;font-family:"Libre Franklin",Arial,sans-serif;color:var(--grey-text)}
.abs{position:absolute}

.top-bar{left:0;top:0;width:1200px;height:3px;background:var(--orange)}
.site-header{left:0;top:3px;width:1200px;height:71px;background:var(--white);box-shadow:0 2px 6px rgba(0,0,0,.05);z-index:2}
.brand{left:206px;top:16px;display:flex;align-items:center;gap:8px;color:var(--orange);font-weight:500;font-size:22px;letter-spacing:2px}
.brand-dot{width:14px;height:14px;border-radius:50%;background:var(--orange)}
.contact-line{right:147px;top:18px;font-size:11px;font-weight:600;color:var(--orange);display:flex;gap:18px}
.main-nav{right:147px;top:42px;display:flex;gap:14px;font-size:10px;letter-spacing:1px;font-weight:500;color:#666}
.main-nav .active{color:#222;font-weight:700;position:relative}
.main-nav .active::after{content:"";position:absolute;left:0;right:0;top:23px;height:2px;background:#444}

.hero{left:0;top:74px;width:1200px;height:374px;background:linear-gradient(#f1f1f1,var(--white) 20%,var(--white) 85%,#eee);overflow:hidden}
.product-mark{left:325px;top:54px;width:90px;height:90px;border:8px solid var(--orange);border-radius:50%}
.tagline{left:284px;top:180px;width:196px;text-align:center;font-size:10px;line-height:13px;color:#666}
.vertical-label{left:486px;top:150px;width:148px;transform-origin:0 0;transform:rotate(-90deg) translate(-146px,0);font-size:9px;font-weight:700;letter-spacing:1px;color:#222;white-space:nowrap}
.hero-frame-back{left:558px;top:32px;width:436px;height:300px;border:1px solid #e4e4e4;background:#fafafa}
.hero-card{left:573px;top:48px;width:438px;height:280px;background:var(--white);box-shadow:0 2px 10px rgba(0,0,0,.12);padding:6px}
.hero-photo{width:100%;height:100%;background:linear-gradient(135deg,#e8e8e8 0%,#bdbdbd 45%,#d8b878 62%,#8a8a8a 100%)}
.hero-word{left:208px;top:278px;font-family:"Archivo Black",Arial,sans-serif;font-size:104px;line-height:1;color:var(--grey-light);letter-spacing:-2px}

.video-back{left:248px;top:501px;width:298px;height:189px;border:1px solid #e6e6e6}
.video-card{left:266px;top:520px;width:299px;height:191px;background:var(--white);box-shadow:0 2px 10px rgba(0,0,0,.14)}
.video-photo{left:118px;top:10px;width:175px;height:176px;background:linear-gradient(180deg,#e9e1dc 0%,#d4c1b5 35%,#8e8e8a 60%,#7b7d79 100%);border-radius:40% 40% 0 0}
.play-btn{left:121px;top:75px}
.speaker{left:19px;top:147px;font-size:11px;color:#333;line-height:11px}
.speaker small{display:block;font-size:8px;color:#666;line-height:10px;margin-top:2px}

.section-title{font-family:"Montserrat",Arial,sans-serif;font-weight:500;color:var(--grey-head);font-size:42px;letter-spacing:1px;line-height:1}
.underline{height:3px;background:var(--orange)}
.who-title{left:612px;top:518px}
.who-underline{left:611px;top:569px;width:127px}
.who-text{left:611px;top:590px;width:390px;font-size:10.5px;line-height:14.4px;color:#555}
.btn{left:612px;top:670px;width:131px;height:35px;background:var(--orange);color:var(--white);font-weight:700;font-size:12px;display:flex;align-items:center;justify-content:center;border-radius:2px;letter-spacing:.3px}

.clients{left:225px;top:722px;width:810px;height:120px;background:linear-gradient(#fff,#f8f8f8);border-bottom:1px dotted #ccc}
.client{top:48px;transform:translateX(-50%);display:flex;align-items:center;gap:4px;font-size:13px;font-weight:600;color:#aaa;white-space:nowrap}
.client i{display:block;width:16px;height:16px;border-radius:50%;background:#c8c8c8}
.client i.sq{border-radius:2px}

.what-title{left:0;width:1236px;text-align:center;top:894px}
.what-underline{left:544px;top:945px;width:127px}
.divider{left:604px;top:970px;width:1px;height:210px;background:var(--line)}
.connector{height:1px;background:var(--line)}
.node{width:8px;height:8px;border-radius:50%;background:var(--line)}
.service-title{font-weight:700;font-size:20px;color:var(--orange)}
.service-text{font-size:10.5px;line-height:14.4px;color:#555}
.advisory-title{right:681px;top:1036px}
.advisory-text{right:680px;top:1074px;width:310px;text-align:right}
.insights-title{left:695px;top:1086px}
.insights-text{left:695px;top:1124px;width:310px}
</style>
</head>
<body>
<div class="abs top-bar"></div>
<header class="abs site-header">
  <div class="abs brand"><span class="brand-dot"></span>TALLYFORM PARTNERS</div>
  <div class="abs contact-line"><span>T: +31(0)6 20485173</span><span>E: hello@tallyformpartners.com</span><span>KvK: 70.38.15.92</span></div>
  <nav class="abs main-nav"><span class="active">HOME</span><span>ABOUT US</span><span>PRODUCTS</span><span>CONTACT US</span></nav>
</header>

<section class="abs hero">
  <div class="abs product-mark"></div>
  <p class="abs tagline">software-as-a-service to capture, learn and target our client’s website visitors and turn them into loyal customers.</p>
  <div class="abs vertical-label">A DATA SCIENCE COMPANY</div>
  <div class="abs hero-frame-back"></div>
  <div class="abs hero-card"><div class="hero-photo" role="img" aria-label="Hands holding a tablet showing bar and pie charts over printed reports and glasses"></div></div>
  <div class="abs hero-word">QUORLINK</div>
</section>

<div class="abs video-back"></div>
<div class="abs video-card">
  <div class="abs video-photo" role="img" aria-label="Video still of a company executive speaking"></div>
  <svg class="abs play-btn" width="42" height="42" viewBox="0 0 42 42"><circle cx="21" cy="21" r="18" fill="#fff" stroke="#111" stroke-width="3.5"/><path d="M16 12 L30 21 L16 30Z" fill="#111"/></svg>
  <div class="abs speaker">Marten Hollis<small>Senior Vice President<br>Design</small></div>
</div>

<h2 class="abs section-title who-title">Who we are?</h2>
<div class="abs underline who-underline"></div>
<p class="abs who-text">We believe that every company needs data science and algorithms to stay on top of today’s overwhelming speed of innovation. We advise and help to turn your company into a data driven company by making data science comprehensible and usable for everybody in your organization.</p>
<div class="abs btn">READ MORE</div>

<div class="abs clients">
  <div class="abs client" style="left:159px">VOLTCELL</div>
  <div class="abs client" style="left:261px"><i class="sq"></i>kestra</div>
  <div class="abs client" style="left:368px">tripleaf</div>
  <div class="abs client" style="left:473px"><i></i>bavaro</div>
  <div class="abs client" style="left:577px"><i class="sq"></i>sunridge</div>
  <div class="abs client" style="left:681px">glaxen</div>
</div>

<h2 class="abs section-title what-title">What do we do?</h2>
<div class="abs underline what-underline"></div>
<div class="abs divider"></div>

<svg class="abs" style="left:436px;top:956px" width="80" height="72" viewBox="0 0 80 72">
  <path d="M40 6 C18 2 4 16 8 34 C10 42 14 46 12 56 L24 46" fill="none" stroke="#bbb" stroke-width="5"/>
  <ellipse cx="50" cy="42" rx="26" ry="20" fill="#bbb"/>
  <path d="M58 58 L66 70 L62 54Z" fill="#bbb"/>
</svg>
<div class="abs connector" style="left:518px;top:994px;width:86px"></div>
<div class="abs node" style="left:515px;top:990px"></div>
<div class="abs service-title advisory-title">Advisory</div>
<p class="abs service-text advisory-text">Data science comes in many flavors. Which one fits your company best? Taking all costs, benefits and organizational impact into account? We can help you with formulating a strategy to make sure you get the most out of your data.</p>

<svg class="abs" style="left:694px;top:990px" width="76" height="80" viewBox="0 0 76 80">
  <g stroke="#aaa" stroke-width="3" fill="none">
    <line x1="34" y1="46" x2="62" y2="14"/><line x1="34" y1="46" x2="14" y2="16"/><line x1="34" y1="46" x2="12" y2="54"/><line x1="34" y1="46" x2="62" y2="60"/><line x1="34" y1="46" x2="38" y2="70"/>
    <circle cx="34" cy="46" r="7" fill="#fff"/><circle cx="62" cy="14" r="6" fill="#fff"/><circle cx="38" cy="70" r="6" fill="#fff"/>
  </g>
  <circle cx="14" cy="16" r="5" fill="#aaa"/><circle cx="12" cy="54" r="5" fill="#aaa"/><circle cx="62" cy="60" r="5" fill="#aaa"/>
</svg>
<div class="abs connector" style="left:604px;top:1037px;width:86px"></div>
<div class="abs node" style="left:686px;top:1033px"></div>
<div class="abs service-title insights-title">Insights</div>
<p class="abs service-text insights-text">We can give you the insights you need to manage your business. We can deliver the technology or the voice-over to your business performance. We believe in do-it-yourself analytics, whereby we give you the keys to your own data.</p>
</body>
</html>
```